VKTO Meridian LLC Website

Basic website for a start up business in the defense and federal space. If we could have intelligence analysis and technology as a focus that would be great. Looking to use our core colors but a lighter set of web pages would be preferable

Target Market(s)

Defense

Coding

Coded - Design and coding required

Number of Pages Required

3 page

```html
<!DOCTYPE html>
<html lang="en">
<head>
<meta charset="utf-8">
<title>VKTO Meridian LLC</title>
<link href="https://fonts.googleapis.com/css2?family=Lato:wght@400;700&family=Roboto:wght@400;500&display=swap" rel="stylesheet">
<style>
:root{
  --red:#c8003c;
  --red-dark:#8e0029;
  --ink:#1d1d1f;
  --black:#000;
  --white:#fff;
  --navy:#142238;
  --navy-deep:#0a1422;
  --grey:#555;
  --line:#c9c9c9;
}
*{box-sizing:border-box;margin:0;padding:0}
html,body{width:1200px;height:3393px;overflow:hidden}
body{position:relative;background:var(--white);font-family:"Lato",sans-serif;color:var(--ink)}
.abs{position:absolute}
.btn{position:absolute;display:flex;align-items:center;justify-content:center;gap:8px;background:var(--red);color:var(--white);border-radius:23px;font:500 14px "Roboto",sans-serif;text-transform:uppercase}
.btn.dark{background:var(--black)}
h2{font:400 40px "Roboto",sans-serif;text-transform:uppercase;letter-spacing:.3px}
.rule{position:absolute;height:3px;width:100px;background:var(--red)}
p.copy{font-size:13.5px;line-height:25.7px;text-align:justify}
/* header */
.logo{position:absolute;left:112px;top:34px;font:400 32px "Roboto",sans-serif;color:var(--white);letter-spacing:1px}
.nav{position:absolute;left:408px;top:44px;display:flex;gap:26px;font:400 14px "Roboto",sans-serif;color:var(--white);text-transform:uppercase}
.nav .on{border-bottom:2px solid var(--red);padding-bottom:3px}
.arrow{position:absolute;width:44px;height:44px;border-radius:50%;background:rgba(0,0,0,.55);display:flex;align-items:center;justify-content:center}
/* services */
.svc{position:absolute;width:324px;height:324px;border-radius:50%;color:var(--white);text-align:center;padding-top:38px}
.svc h3{font:500 21px "Roboto",sans-serif;margin:14px 0 12px}
.svc p{font-size:13px;line-height:25.7px;padding:0 44px}
.svc .go{width:18px;height:18px;margin:10px auto 0;display:block}
/* form */
.field{position:absolute;border:1px solid var(--line);border-radius:4px;font:400 14px "Roboto",sans-serif;color:#444;padding:19px 23px}
.field.active{border-color:var(--red);color:var(--red)}
.contact{position:absolute;width:300px;text-align:center}
.contact .dot{width:80px;height:80px;border-radius:50%;background:var(--red);margin:0 auto;display:flex;align-items:center;justify-content:center}
.contact h4{font:400 21px "Roboto",sans-serif;margin-top:14px;color:#333}
.contact small{display:block;font-size:13px;margin-top:8px}
/* footer */
.fnav{position:absolute;top:3230px;left:0;width:1200px;text-align:center;font:400 14px "Roboto",sans-serif;color:var(--white);text-transform:uppercase;word-spacing:2px}
.social{position:absolute;top:3276px;left:514px;display:flex;gap:14px}
.social span{width:30px;height:30px;border-radius:50%;background:var(--white)}
.social span.on{background:var(--red)}
.legal{position:absolute;top:3328px;width:1200px;text-align:center;font-size:14px;color:var(--white)}
.legal a{color:var(--red);text-decoration:none}
</style>
</head>
<body>

<!-- HERO -->
<svg class="abs" style="left:0;top:0" width="1200" height="640" viewBox="0 0 1200 640">
  <defs>
    <linearGradient id="heroTone" x1="0" y1="0" x2="1" y2="1">
      <stop offset="0" stop-color="#2a4a74"/><stop offset=".5" stop-color="#1a2c46"/><stop offset="1" stop-color="#0c1626"/>
    </linearGradient>
  </defs>
  <rect width="1200" height="640" fill="url(#heroTone)" role="img" aria-label="Photo of an officer briefing analysts in a command room with world map screens"/>
  <path d="M0 640 L0 625 C300 520 500 470 650 470 C850 470 1080 530 1200 640 Z" fill="var(--white)"/>
  <path d="M100 605 C350 500 540 468 680 470 C900 472 1100 530 1170 610 C1080 540 900 490 690 488 C520 488 330 530 100 605 Z" fill="var(--red)"/>
</svg>
<div class="logo">VKTO Meridian</div>
<nav class="nav"><span class="on">Home</span><span>About Us</span><span>Work With Us</span><span>News</span><span>Contact Us</span></nav>
<div class="btn" style="left:913px;top:30px;width:175px;height:44px">
  <svg width="12" height="12" viewBox="0 0 24 24"><path fill="#fff" d="M6.6 10.8a15 15 0 006.6 6.6l2.2-2.2a1 1 0 011-.25 11 11 0 003.6.6 1 1 0 011 1V20a1 1 0 01-1 1A17 17 0 013 4a1 1 0 011-1h3.5a1 1 0 011 1c0 1.25.2 2.45.6 3.6a1 1 0 01-.25 1z"/></svg>+1 888 888 8888</div>
<div class="abs" style="left:0;top:230px;width:1200px;text-align:center;font:500 52px 'Roboto',sans-serif;color:#fff">VKTO MERIDIAN LLC</div>
<div class="btn" style="left:525px;top:300px;width:150px;height:44px">Get Started</div>
<div class="arrow" style="left:31px;top:240px"><svg width="10" height="14" viewBox="0 0 10 14"><path d="M7 2L2 7l5 5" stroke="#fff" stroke-width="2" fill="none"/></svg></div>
<div class="arrow" style="left:1119px;top:240px"><svg width="10" height="14" viewBox="0 0 10 14"><path d="M3 2l5 5-5 5" stroke="#fff" stroke-width="2" fill="none"/></svg></div>

<!-- WHO WE ARE -->
<h2 class="abs" style="left:112px;top:660px">Who We Are</h2>
<div class="rule" style="left:112px;top:716px"></div>
<div class="abs" style="left:112px;top:734px;width:462px">
  <p class="copy">Lorem ipsum dolor sit amet, consectetur adipiscing elit, sed do eiusmod tempor incididunt ut labore et dolore magna aliqua. Ut enim ad minim veniam, quis nostrud exercitation ullamco laboris nisi ut aliquip ex ea commodo consequat. Duis aute irure dolor in reprehenderit in voluptate velit esse cillum dolore eu fugiat nulla pariatur.</p>
  <p class="copy" style="margin-top:25px">Excepteur sint occaecat cupidatat non proident, sunt in culpa qui officia deserunt mollit anim id est laborum. Lorem ipsum dolor sit amet, conse ctetur adipiscing elit, sed do eiusmod tempor</p>
</div>
<div class="btn" style="left:112px;top:984px;width:150px;height:44px">Get Started</div>
<svg class="abs" style="left:590px;top:630px" width="550" height="460" viewBox="0 0 550 460">
  <defs><linearGradient id="skyTone" x1="0" y1="0" x2="0" y2="1"><stop offset="0" stop-color="#8a96a8"/><stop offset=".45" stop-color="#d99a6a"/><stop offset="1" stop-color="#7f8ea3"/></linearGradient></defs>
  <path d="M16 10 L122 10 L16 114 Z" fill="var(--red)"/>
  <rect x="42" y="35" width="456" height="363" rx="6" fill="url(#skyTone)" role="img" aria-label="Photo of fighter jets flying above clouds at sunset"/>
  <path d="M362 274 L540 274 L500 300 C430 390 280 450 30 420 L5 408 C250 440 400 400 470 300 L362 300 Z" fill="var(--red)"/>
  <path d="M362 274 L540 274 L520 287 L372 287 Z" fill="var(--white)"/>
</svg>

<!-- WHAT WE DO -->
<h2 class="abs" style="left:0;top:1172px;width:1200px;text-align:center">What We Do</h2>
<div class="rule" style="left:551px;top:1228px"></div>

<!-- RED BAND -->
<svg class="abs" style="left:0;top:1300px" width="1200" height="1030" viewBox="0 0 1200 1030">
  <defs><linearGradient id="redTone" x1="0" y1="0" x2="0" y2="1"><stop offset="0" stop-color="#c8003c"/><stop offset=".55" stop-color="#b0073a"/><stop offset="1" stop-color="#c3103f"/></linearGradient></defs>
  <path d="M0 40 C60 130 200 140 300 130 L900 130 C1000 110 1100 70 1200 40 L1200 1030 L0 1030 Z" fill="url(#redTone)" role="img" aria-label="Faint background photo of military aircraft on a hangar floor"/>
  <path d="M30 75 C60 110 80 120 100 130 L95 138 C70 125 50 105 30 75 Z" fill="var(--black)"/>
  <path d="M0 1030 L0 1000 C250 900 480 870 650 870 C850 870 1050 920 1200 1025 L1200 1030 Z" fill="var(--white)"/>
  <path d="M90 1005 C330 910 520 878 680 874 C900 870 1090 930 1168 1000 C1080 950 900 895 690 893 C520 893 330 930 90 1005 Z" fill="var(--black)"/>
</svg>

<!-- service circles -->
<svg class="abs" style="left:80px;top:1235px" width="1040" height="390" viewBox="0 0 1040 390">
  <circle cx="194" cy="194" r="184" fill="#fff"/><circle cx="520" cy="194" r="184" fill="#fff"/><circle cx="846" cy="194" r="184" fill="#fff"/>
</svg>
<div class="svc" style="left:112px;top:1267px;background:var(--black)">
  <svg width="74" height="82" viewBox="0 0 74 82"><path d="M37 3 L68 14 V40 C68 60 54 74 37 79 C20 74 6 60 6 40 V14 Z" fill="none" stroke="#fff" stroke-width="4"/><path d="M37 14 L58 22 V40 C58 54 49 64 37 68 C25 64 16 54 16 40 V22 Z" fill="none" stroke="#fff" stroke-width="3"/><path d="M37 28l4 9 10 1-7 7 2 10-9-5-9 5 2-10-7-7 10-1z" fill="none" stroke="#fff" stroke-width="3"/></svg>
  <h3>Nemo enim ipsam</h3>
  <p>Lorem ipsum dolor sit amet, consectetur adipiscing elit, sed do eiusmod tempor incididunt ut labore et dolore</p>
  <svg class="go" viewBox="0 0 18 18"><circle cx="9" cy="9" r="9" fill="#fff"/><path d="M7 5l4 4-4 4" stroke="#000" stroke-width="2" fill="none"/></svg>
</div>
<div class="svc" style="left:438px;top:1267px;background:var(--red)">
  <svg width="80" height="80" viewBox="0 0 80 80"><path d="M6 24 L40 6 L74 24 Z M6 24 H74 V30 H6 Z" fill="none" stroke="#fff" stroke-width="3"/><path d="M14 34v32M26 34v32M40 34v32M54 34v32M66 34v32" stroke="#fff" stroke-width="5"/><rect x="6" y="68" width="68" height="6" fill="none" stroke="#fff" stroke-width="3"/></svg>
  <h3>Nemo enim ipsam</h3>
  <p>Lorem ipsum dolor sit amet, consectetur adipiscing elit, sed do eiusmod tempor incididunt ut labore et dolore</p>
  <svg class="go" viewBox="0 0 18 18"><circle cx="9" cy="9" r="9" fill="#fff"/><path d="M7 5l4 4-4 4" stroke="var(--red)" stroke-width="2" fill="none"/></svg>
</div>
<div class="svc" style="left:764px;top:1267px;background:var(--black)">
  <svg width="80" height="80" viewBox="0 0 80 80"><path d="M8 4 H50 V30 M8 4 V70 H30" fill="none" stroke="#fff" stroke-width="3"/><path d="M16 16h26M16 26h20M16 36h12" stroke="#fff" stroke-width="3"/><rect x="30" y="38" width="44" height="36" rx="3" fill="none" stroke="#fff" stroke-width="3"/><path d="M44 38v-6h16v6M30 52h44" stroke="#fff" stroke-width="3" fill="none"/><rect x="48" y="48" width="8" height="8" fill="none" stroke="#fff" stroke-width="3"/><circle cx="64" cy="16" r="6" fill="none" stroke="#fff" stroke-width="3"/></svg>
  <h3>Nemo enim ipsam</h3>
  <p>Lorem ipsum dolor sit amet, consectetur adipiscing elit, sed do eiusmod tempor incididunt ut labore et dolore</p>
  <svg class="go" viewBox="0 0 18 18"><circle cx="9" cy="9" r="9" fill="#fff"/><path d="M7 5l4 4-4 4" stroke="#000" stroke-width="2" fill="none"/></svg>
</div>

<!-- WHY CHOOSE US -->
<div class="abs" style="left:112px;top:1688px;width:465px;height:393px;border-radius:30px;background:var(--black);padding:6px">
  <div style="width:100%;height:100%;border:3px solid #fff;border-radius:26px;background:linear-gradient(120deg,#3d5876,#1b2a3d 55%,#0d1724)" role="img" aria-label="Photo of an officer pointing at world map screens during a briefing"></div>
</div>
<h2 class="abs" style="left:611px;top:1678px;color:#fff">Why Choose Us</h2>
<div class="abs" style="left:611px;top:1747px;width:477px;color:#fff">
  <p class="copy">Lorem ipsum dolor sit amet, consectetur adipiscing elit, sed do eiusmod tempor incididunt ut labore et dolore magna aliqua. Ut enim ad minim veniam, quis nostrud exercitation ullamco laboris nisi ut aliquip ex ea commodo consequat. Duis aute irure dolor in reprehenderit in voluptate velit esse cillum dolore eu fugiat nulla pariatur.</p>
  <p class="copy" style="margin-top:25px">Excepteur sint occaecat cupidatat non proident, sunt in culpa qui officia deserunt mollit anim id est laborum. Lorem ipsum dolor sit amet, conse ctetur adipiscing elit, sed do eiusmod tempor incididunt ut labore et dolore magna aliqua.</p>
</div>
<div class="btn dark" style="left:611px;top:2039px;width:150px;height:44px">Learn More
  <svg width="13" height="13" viewBox="0 0 18 18"><circle cx="9" cy="9" r="9" fill="#fff"/><path d="M7 5l4 4-4 4" stroke="#000" stroke-width="2" fill="none"/></svg></div>

<!-- QUOTE -->
<h2 class="abs" style="left:0;top:2330px;width:1200px;text-align:center">Get A Free Quote</h2>
<div class="rule" style="left:551px;top:2384px"></div>
<div class="field active" style="left:158px;top:2417px;width:284px;height:56px">Name*</div>
<div class="field" style="left:458px;top:2417px;width:284px;height:56px">Email*</div>
<div class="field" style="left:757px;top:2417px;width:285px;height:56px">Phone*</div>
<div class="field" style="left:158px;top:2489px;width:884px;height:168px">Message*</div>
<div class="btn" style="left:525px;top:2674px;width:150px;height:44px">Submit Now</div>

<div class="contact" style="left:156px;top:2773px">
  <div class="dot"><svg width="18" height="24" viewBox="0 0 18 24"><path d="M9 0a9 9 0 00-9 9c0 7 9 15 9 15s9-8 9-15a9 9 0 00-9-9zm0 12.5A3.5 3.5 0 119 5.5a3.5 3.5 0 010 7z" fill="#fff"/></svg></div>
  <h4>Address :</h4><small>123, Lorem ipsum dolor sit amet,</small>
</div>
<div class="contact" style="left:452px;top:2773px">
  <div class="dot"><svg width="22" height="22" viewBox="0 0 24 24"><path fill="#fff" d="M6.6 10.8a15 15 0 006.6 6.6l2.2-2.2a1 1 0 011-.25 11 11 0 003.6.6 1 1 0 011 1V20a1 1 0 01-1 1A17 17 0 013 4a1 1 0 011-1h3.5a1 1 0 011 1c0 1.25.2 2.45.6 3.6a1 1 0 01-.25 1z"/></svg></div>
  <h4>Phone :</h4><small>+1 888 888 8888</small>
</div>
<div class="contact" style="left:748px;top:2773px">
  <div class="dot"><svg width="26" height="20" viewBox="0 0 26 20"><rect width="26" height="20" rx="2" fill="#fff"/><path d="M1 2l12 9 12-9" stroke="var(--red)" stroke-width="2" fill="none"/></svg></div>
  <h4>Email address :</h4><small>info@companyname.com</small>
</div>

<!-- FOOTER -->
<svg class="abs" style="left:0;top:2920px" width="1200" height="473" viewBox="0 0 1200 473">
  <defs><linearGradient id="footTone" x1="0" y1="0" x2="1" y2="1"><stop offset="0" stop-color="#17222b"/><stop offset="1" stop-color="#090d12"/></linearGradient></defs>
  <rect width="1200" height="473" fill="url(#footTone)" role="img" aria-label="Dark background photo of an operations centre with monitors"/>
  <path d="M0 0 H1200 V15 C1000 120 800 165 600 165 C380 165 180 110 0 25 Z" fill="var(--white)"/>
  <path d="M30 18 C200 110 400 150 600 152 C800 154 960 110 1095 20 C980 70 820 128 600 128 C400 128 220 90 30 18 Z" fill="var(--red)"/>
</svg>
<div class="abs" style="left:0;top:3148px;width:1200px;text-align:center;font:400 34px 'Roboto',sans-serif;color:#fff;letter-spacing:1px">VKTO Meridian</div>
<div class="fnav">Home &nbsp;/&nbsp; About Us &nbsp;/&nbsp; Work With Us &nbsp;/&nbsp; News &nbsp;/&nbsp; Contact Us</div>
<div class="social"><span></span><span></span><span class="on"></span><span></span></div>
<div class="legal">© Copyright 2022 <a>VKTO Meridian LLC</a> All Rights Reserved.</div>

</body>
</html>
```